Velorik Cement

i need envelope a4 size and normal size - folder -paper bag - business card -
letterhead

Stationery Design project 'Stationery velorik cement : letterhead ,folder,business card ,envelope ,envelope A4size .paper bag '

Target Market(s)

ready mix concrete

Font styles to use
Serif

Colors

Designer to choose colors to be used in the design.

Requirements
Must have
• nice design

```html
<!DOCTYPE html>
<html lang="en">
<head>
<meta charset="utf-8">
<title>Velorik Cement – Business Card</title>
<link href="https://fonts.googleapis.com/css2?family=Source+Sans+3:wght@400;600;700&display=swap" rel="stylesheet">
<style>
  :root {
    --brand-blue: #02508a;
    --brand-grey: #7f8083;
    --card-white: #f4f6f9;
    --card-shade: #e2e7ee;
    --backdrop: #e4e4e6;
    --text-dark: #3a3d42;
    --divider: #c4c9d0;
  }
  * { margin: 0; padding: 0; box-sizing: border-box; }
  html, body {
    width: 1200px; height: 906px; overflow: hidden;
    background: var(--backdrop);
    font-family: "Source Sans 3", Arial, sans-serif;
  }
  .sheet {
    position: relative; width: 1200px; height: 906px;
    display: flex; align-items: center; justify-content: center; gap: 48px;
  }
  .card {
    position: relative; width: 540px; height: 310px; overflow: hidden;
    background: linear-gradient(135deg, var(--card-white), var(--card-shade));
    box-shadow: 0 10px 24px rgba(0,0,0,0.12);
  }
  .card__shapes { position: absolute; inset: 0; width: 100%; height: 100%; }
  .wordmark {
    position: absolute; display: flex; align-items: center; gap: 10px;
    font-weight: 700; letter-spacing: 1px; white-space: nowrap;
  }
  .wordmark__dot { border-radius: 50%; flex: none; }
  .card--front .wordmark { left: 40px; top: 176px; font-size: 30px; color: #fff; }
  .card--front .wordmark__dot { width: 22px; height: 22px; background: #fff; }
  .card--back .wordmark { left: 32px; top: 140px; font-size: 20px; color: var(--brand-blue); }
  .card--back .wordmark__dot { width: 14px; height: 14px; background: var(--brand-blue); }
  .divider {
    position: absolute; left: 264px; top: 56px; width: 1px; height: 160px;
    background: var(--divider);
  }
  .contact { position: absolute; left: 284px; top: 60px; color: var(--text-dark); }
  .contact__name {
    font-size: 19px; font-weight: 700; color: var(--brand-blue); letter-spacing: 0.3px;
  }
  .contact__role { font-size: 13px; margin-top: 1px; }
  .contact__list { list-style: none; margin-top: 12px; }
  .contact__item {
    display: flex; align-items: center; gap: 8px; font-size: 13px; line-height: 19px;
  }
  .contact__item svg { width: 12px; height: 12px; flex: none; }
  .contact__address { font-size: 13px; line-height: 17px; margin-top: 12px; padding-left: 20px; }
</style>
</head>
<body>
<main class="sheet">

  <section class="card card--front" aria-label="Business card front">
    <svg class="card__shapes" viewBox="0 0 540 310" preserveAspectRatio="none">
      <polygon points="0,0 210,0 490,205 160,310 0,310" fill="var(--brand-blue)"/>
      <polygon points="540,0 540,200 500,208 290,110" fill="var(--brand-grey)"/>
    </svg>
    <div class="wordmark"><span class="wordmark__dot"></span>VELORIK CEMENT</div>
  </section>

  <section class="card card--back" aria-label="Business card back">
    <svg class="card__shapes" viewBox="0 0 540 310" preserveAspectRatio="none">
      <polygon points="540,170 540,232 370,248" fill="var(--brand-grey)"/>
      <polygon points="0,272 540,222 540,232 190,310 0,310" fill="var(--brand-blue)"/>
    </svg>
    <div class="wordmark"><span class="wordmark__dot"></span>VELORIK CEMENT</div>
    <div class="divider"></div>
    <div class="contact">
      <p class="contact__name">DANIEL HARWOOD</p>
      <p class="contact__role">General Manager</p>
      <ul class="contact__list">
        <li class="contact__item">
          <svg viewBox="0 0 12 12"><path d="M2.5 1h2l1 2.6-1.3 1a6 6 0 0 0 3.2 3.2l1-1.3L11 7.5v2A1.5 1.5 0 0 1 9.5 11 8.5 8.5 0 0 1 1 2.5 1.5 1.5 0 0 1 2.5 1z" fill="var(--brand-blue)"/></svg>
          +964 (0) 750 000 4815
        </li>
        <li class="contact__item">
          <svg viewBox="0 0 12 12"><rect x="0.5" y="2" width="11" height="8" fill="var(--brand-blue)"/><path d="M0.5 2 6 6.5 11.5 2" fill="none" stroke="#fff" stroke-width="1"/></svg>
          info@velorik-cement.com
        </li>
        <li class="contact__item">
          <svg viewBox="0 0 12 12" fill="none" stroke="var(--brand-blue)" stroke-width="1"><circle cx="6" cy="6" r="5"/><ellipse cx="6" cy="6" rx="2.2" ry="5"/><path d="M1 6h10M2 3.3h8M2 8.7h8"/></svg>
          www.velorik-cement.com
        </li>
      </ul>
      <p class="contact__address">Industrial Area No.7<br>Harlan City</p>
    </div>
  </section>

</main>
</body>
</html>
```